parts and kits

we need an updated flyer to email to our customers
we need to have what we sell at kivo
caliper pistons
seal kits
new brake cylinders
brake boosters
brake shoes
brake pads
brake hoses
cables -accelerator, clutch, hand brake etc
for both private, vintage and commercial vehicles

```html
<!DOCTYPE html>
<html lang="en">
<head>
<meta charset="utf-8">
<title>Kivo Auto Centre – Parts and Kits Flyer</title>
<link rel="stylesheet" href="https://fonts.googleapis.com/css2?family=Archivo:wdth,wght@125,900&family=Archivo+Black&family=Anton&family=Roboto:ital,wght@0,300;0,400;1,400&family=Montserrat:wght@500;600&display=swap">
<style>
  :root {
    --black: #000000;
    --olive: #524300;
    --yellow: #f9f200;
    --band-yellow: #f3cf2c;
    --strip-yellow: #ffcb05;
    --red: #ee1111;
    --white: #ffffff;
    --paper: #f4f4f4;
    --swoosh: #e6e6e6;
    --ink: #111111;
    --placeholder-light: #9a9a9a;
    --placeholder-dark: #6e6e6e;
  }
  * { margin: 0; padding: 0; box-sizing: border-box; }
  html, body { width: 904px; height: 1200px; overflow: hidden; background: var(--paper); }
  .flyer { position: relative; width: 904px; height: 1200px; overflow: hidden; background: var(--paper); font-family: "Roboto", Arial, sans-serif; }

  .header { position: absolute; left: 0; top: 0; width: 904px; height: 333px; background: var(--black); }
  .header-stripe { position: absolute; left: 0; top: 0; }
  .header-rule { position: absolute; left: 0; top: 333px; width: 904px; height: 16px; background: var(--strip-yellow); }

  .brand-name { position: absolute; left: 60px; top: 34px; font-family: "Archivo Black", sans-serif; font-size: 122px; line-height: 1; color: var(--yellow); letter-spacing: -1px; }
  .brand-sub { position: absolute; left: 430px; top: 40px; font-family: "Roboto", sans-serif; font-weight: 300; font-size: 54px; line-height: 48px; color: var(--white); }

  .tagline { position: absolute; left: 61px; top: 159px; width: 390px; height: 64px; background: var(--red); padding: 4px 0 0 10px; font-family: "Archivo", "Archivo Black", sans-serif; font-stretch: 125%; font-weight: 900; font-size: 26px; line-height: 29px; color: var(--white); white-space: nowrap; }
  .coverage { position: absolute; left: 61px; top: 233px; font-weight: 300; font-size: 35px; line-height: 40px; color: var(--white); letter-spacing: 0.5px; white-space: nowrap; }

  .parts-hero { position: absolute; left: 567px; top: 116px; width: 321px; height: 294px; border-radius: 50%; background: radial-gradient(ellipse at 50% 45%, var(--placeholder-light) 0%, var(--placeholder-dark) 100%); }

  .backdrop { position: absolute; left: 0; top: 349px; }

  .intro { position: absolute; left: 0; top: 364px; width: 904px; }
  .intro-lead { position: absolute; left: 50px; top: 0; font-style: italic; font-size: 36px; line-height: 1; color: var(--ink); white-space: nowrap; }
  .intro-focus { position: absolute; left: 42px; top: 31px; font-style: italic; font-size: 55px; line-height: 1; color: var(--red); white-space: nowrap; }

  .product { position: absolute; width: 200px; }
  .product-photo { position: absolute; left: 10px; width: 180px; border-radius: 8px; background: radial-gradient(ellipse at 50% 55%, #5a5a5a 0%, #8c8c8c 45%, rgba(244,244,244,0) 72%); }
  .product-label { position: absolute; left: 0; width: 100%; height: 40px; background: var(--black); color: var(--white); font-family: "Anton", sans-serif; font-size: 27px; line-height: 40px; text-align: center; letter-spacing: 0.3px; white-space: nowrap; }

  .cables { position: absolute; left: 0; top: 934px; width: 904px; text-align: center; padding-left: 14px; font-family: "Anton", sans-serif; font-size: 28px; line-height: 1.1; color: var(--ink); letter-spacing: 0.3px; }
  .vehicles { position: absolute; left: 0; top: 999px; width: 904px; text-align: center; font-weight: 300; font-size: 29px; line-height: 1; color: var(--ink); letter-spacing: 0.5px; white-space: nowrap; }

  .promise { position: absolute; left: 0; top: 1041px; width: 904px; height: 106px; background: var(--band-yellow); }
  .promise-quote { position: absolute; left: 0; top: 17px; width: 904px; text-align: center; font-family: "Montserrat", sans-serif; font-weight: 600; font-size: 30px; line-height: 36px; color: var(--ink); white-space: nowrap; }
  .footer { position: absolute; left: 0; top: 1147px; width: 904px; height: 53px; background: var(--black); color: var(--white); text-align: center; font-family: "Montserrat", sans-serif; font-weight: 500; font-size: 18px; line-height: 53px; letter-spacing: 8px; }
</style>
</head>
<body>
<main class="flyer">
  <svg class="backdrop" width="904" height="692" viewBox="0 0 904 692" aria-hidden="true">
    <rect width="904" height="692" fill="#f6f6f6"/>
    <path d="M0 370 C 250 150, 600 60, 904 80 L904 40 C 600 30, 250 110, 0 340 Z" fill="var(--swoosh)" opacity="0.7"/>
    <path d="M300 692 C 420 480, 650 230, 904 120 L904 160 C 680 270, 470 480, 380 692 Z" fill="#ebebeb" opacity="0.8"/>
  </svg>

  <header class="header">
    <svg class="header-stripe" width="904" height="333" viewBox="0 0 904 333" aria-hidden="true">
      <polygon points="314,0 739,0 628,333 226,333" fill="var(--olive)"/>
    </svg>
    <h1 class="brand-name">KIVO</h1>
    <p class="brand-sub">AUTO<br>CENTRE</p>
    <p class="tagline">THE BRAKE AND<br>CABLE SPECIALISTS</p>
    <p class="coverage">PARTS FOR MOTORBIKES,<br>CARS, COMMERCIAL ETC....</p>
  </header>
  <div class="header-rule"></div>

  <div class="parts-hero" role="img" aria-label="Photo collage of assorted car parts arranged around a brake disc"></div>

  <section class="intro">
    <p class="intro-lead">Specialise in the Re-manufacture of</p>
    <p class="intro-focus">Brakes, Hoses &amp; Cables</p>
  </section>

  <section class="products">
    <div class="product" style="left:31px;top:500px">
      <div class="product-photo" style="top:0;height:150px" role="img" aria-label="Black brake caliper with pistons"></div>
      <p class="product-label" style="top:162px;width:198px">CALIPER PISTONS</p>
    </div>
    <div class="product" style="left:243px;top:500px">
      <div class="product-photo" style="top:0;height:150px" role="img" aria-label="Seal kit with gaskets, rings and piston parts"></div>
      <p class="product-label" style="top:162px;width:197px">SEAL KITS</p>
    </div>
    <div class="product" style="left:454px;top:500px">
      <div class="product-photo" style="top:0;height:150px" role="img" aria-label="Brake cylinder assembly"></div>
      <p class="product-label" style="top:162px;width:204px">BRAKE CYLINDERS</p>
    </div>
    <div class="product" style="left:673px;top:500px">
      <div class="product-photo" style="top:0;height:150px" role="img" aria-label="Black brake booster"></div>
      <p class="product-label" style="top:162px;width:198px">BRAKE BOOSTERS</p>
    </div>

    <div class="product" style="left:31px;top:735px">
      <div class="product-photo" style="top:0;height:130px" role="img" aria-label="Pair of drum brake shoes"></div>
      <p class="product-label" style="top:137px;width:198px">BRAKE SHOES</p>
    </div>
    <div class="product" style="left:243px;top:735px">
      <div class="product-photo" style="top:0;height:130px" role="img" aria-label="Set of four disc brake pads"></div>
      <p class="product-label" style="top:137px;width:197px">BRAKE PADS</p>
    </div>
    <div class="product" style="left:454px;top:735px">
      <div class="product-photo" style="top:0;height:130px" role="img" aria-label="Assorted braided brake hoses"></div>
      <p class="product-label" style="top:137px;width:204px">BRAKE HOSES</p>
    </div>
    <div class="product" style="left:673px;top:735px">
      <div class="product-photo" style="top:0;height:130px" role="img" aria-label="Clutch plate and pressure plate"></div>
      <p class="product-label" style="top:137px;width:198px">CLUTCH</p>
    </div>
  </section>

  <p class="cables">CABLES -ACCELERATOR, HAND BRAKE etc...</p>
  <p class="vehicles">FOR BOTH PRIVATE, VINTAGE AND COMMERCIAL VEHICLES</p>

  <section class="promise">
    <p class="promise-quote">&ldquo;Our Aim Is To Repair Parts With The<br>&nbsp;&nbsp;&nbsp;Quickest Turn-around Times Possible&rdquo;</p>
  </section>

  <footer class="footer">WWW.YOURWEBSITE.COM</footer>
</main>
</body>
</html>
```